New AI Company Needs a Powerpoint

We are a new type of AI company called PalvoraAI. Our AI uses human inspired approaches and put the human on the center of all our solutions. We need a standard company powerpoint design to use with potential investors, customers and partners to introduce our company and explain how the approach we take to AI is very different than others.
We want a design that is clean, modern, and playful. We do not want it to look overly robotic or cliche techy. Our mission is to remind the world that technology is a tool to be used to enhance and assist not to replace real humans.
We want a design that can show boring things (like financial info) in engaging ways.

Please use colors in logo variations along with a vibrant complementary color palette of your choosing,

Industry/Entity Type

Technology

Font styles to use
Sans Serif
Other font styles liked:
• Opensans

Colors
0054AA
0677BA
7BADD7
CADEEF
E8F1F8
0094D4
00A9DD
6FCCEA
C7EBF8
E9F6FB
00AB8E
00BBA5
67D7C9
C6EFE9
E9F9F6
59FF00
82FF00
B8FF75
E3FFCB
F4FFEA

Requirements
Must have
• Must incorporate logo colors and style

```html
<!DOCTYPE html>
<html lang="en">
<head>
<meta charset="utf-8">
<title>PalvoraAI – Introduction Slide</title>
<link href="https://fonts.googleapis.com/css2?family=Noto+Sans:wght@400;800&display=swap" rel="stylesheet">
<style>
  :root {
    --ink: #1f2226;
    --sky-wash-top: #e4eef3;
    --sky-wash-bottom: #d6e7ef;
    --accent-blue: #00a3d0;
    --accent-blue-soft: rgba(0, 163, 208, 0.5);
    --accent-blue-faint: rgba(0, 163, 208, 0.12);
    --accent-blue-clear: rgba(0, 163, 208, 0);
    --accent-green: #00ab6f;
  }
  html, body {
    margin: 0;
    padding: 0;
    width: 1200px;
    height: 675px;
    overflow: hidden;
  }
  .slide {
    position: relative;
    width: 1200px;
    height: 675px;
    overflow: hidden;
    background: linear-gradient(160deg, var(--sky-wash-top) 0%, #e9f1f5 45%, var(--sky-wash-bottom) 100%);
    font-family: "Noto Sans", sans-serif;
    color: var(--ink);
  }
  .brand-artwork {
    position: absolute;
    right: 0;
    top: 0;
    width: 640px;
    height: 675px;
    background: radial-gradient(ellipse 60% 45% at 100% 48%,
      var(--accent-blue) 0%,
      var(--accent-blue-soft) 40%,
      var(--accent-blue-faint) 75%,
      var(--accent-blue-clear) 100%);
  }
  .slide-title {
    position: absolute;
    left: 128px;
    top: 138px;
    margin: 0;
    display: flex;
    align-items: flex-end;
    gap: 30px;
  }
  .slide-title .company-name {
    font-size: 68px;
    font-weight: 400;
    line-height: 1;
    letter-spacing: 0.5px;
    color: var(--ink);
    padding-bottom: 6px;
  }
  .slide-title .title-mark {
    font-size: 118px;
    font-weight: 800;
    line-height: 0.85;
    color: var(--accent-green);
  }
  .intro-copy {
    position: absolute;
    left: 130px;
    top: 280px;
    width: 780px;
  }
  .intro-copy p {
    margin: 0 0 36px;
    font-size: 28px;
    line-height: 36px;
    font-weight: 400;
  }
</style>
</head>
<body>
  <main class="slide">
    <div class="brand-artwork" role="img" aria-label="Decorative blue brand artwork with curved connector lines and angular shapes"></div>

    <h1 class="slide-title">
      <span class="company-name">PalvoraAI</span>
      <span class="title-mark">?</span>
    </h1>

    <section class="intro-copy">
      <p>We are a new type of AI company called PalvoraAI. Our AI uses human inspired approaches and put the human on the center of all our solutions.</p>
      <p>We are a new type of AI company called PalvoraAI. Our AI uses human inspired approaches.</p>
    </section>
  </main>
</body>
</html>
```